Restaurant needs a vertical banner for fried catfish

Our restaurant is looking for an eye-catching 78.75in. x 36in. vertical physical banner ad for our fried catfish. Photos for the fried catfish will be provided as a reference but we will also accept anything similar to the photo. We will be using the following as our receptacle: https://www.plankoria.example/banner-stand/retractable-banner-stands/
The design must incorporate the following flavor texts:
Fried Catfish
Always Fresh!
Made from Scratch
Hand-cut Fillets
The Best Catfish in Texas
Served with fries, hush puppies, and a 32oz fountain drink
Also available by the pound!
The final design should be creative, professional, and eye-catching for customers.
Updates
Colors
Designer to choose colors to be used in the design.
Requirements
Must have
- We are open to any and all design elements, albeit the 'flavor texts' should not overpower, but complement the fried catfish photo. 'Fried Catfish' can be used in lieu of a main title/logo.
Nice to have
- Transparent or textured backgrounds that can encompass any or all part of the banner such as a cutting board, shadows, abstract, etc to show depth are a plus.
- Use of vectors or objects such as ribbons or shapes to encapsulate the 'flavor texts' are also encouraged.

```html
<!DOCTYPE html>
<html lang="en">
<head>
<meta charset="UTF-8">
<title>Fried Catfish – Always Fresh!</title>
<link rel="stylesheet" href="https://fonts.googleapis.com/css2?family=Bitter:ital,wght@0,800;1,800&family=Bebas+Neue&display=swap">
<style>
  :root {
    --green: #0f6e4b;
    --ink: #1e1610;
    --utensil: #6a4322;
    --yellow: #f3d31c;
    --paper-top: #ecd3ae;
    --paper-mid: #c99677;
    --paper-low: #e2bf98;
    --dash: #2a2018;
  }
  * { margin: 0; padding: 0; box-sizing: border-box; }
  html, body { width: 1200px; height: 2624px; overflow: hidden; }
  body { background: var(--paper-top); }
  .banner {
    position: relative;
    width: 1200px; height: 2624px; overflow: hidden;
    background: linear-gradient(180deg, var(--paper-top) 0%, #e3c29c 45%, var(--paper-mid) 62%, #d6aa88 78%, var(--paper-low) 100%);
  }
  .cut-line {
    position: absolute; left: 70px; top: 38px; width: 1076px; height: 2547px;
    border: 4px dashed var(--dash);
  }
  .hero { position: absolute; left: 0; top: 0; width: 1200px; height: 1300px; }
  .title-block {
    position: absolute; left: 600px; top: 255px;
    transform: translate(-50%, -50%) rotate(-14deg);
    text-align: center; white-space: nowrap;
  }
  .title {
    font-family: 'Bitter', serif; font-weight: 800;
    font-size: 112px; line-height: 1; color: var(--green);
    letter-spacing: 2px;
  }
  .tagline {
    font-family: 'Bitter', serif; font-weight: 800;
    font-size: 44px; line-height: 1.1; color: var(--ink);
    letter-spacing: 1px; margin-top: 4px;
  }
  .features { position: absolute; left: 0; top: 1190px; width: 1200px; text-align: center; }
  .feature { display: flex; flex-direction: column; align-items: center; }
  .utensils { width: 290px; height: 90px; display: block; }
  .feature-text {
    font-family: 'Bebas Neue', sans-serif; font-size: 70px; line-height: 1.45;
    color: var(--ink); letter-spacing: 1px;
  }
  .feature + .feature { margin-top: 46px; }
  .footer-band {
    position: absolute; left: 0; top: 2373px; width: 1200px; height: 112px;
    background: var(--green);
    display: flex; align-items: center; justify-content: center;
    font-family: 'Bitter', serif; font-style: italic; font-weight: 800;
    font-size: 54px; color: var(--yellow); letter-spacing: 1px;
  }
</style>
</head>
<body>
<main class="banner">
  <svg class="hero" viewBox="0 0 1200 1300" aria-hidden="false">
    <defs>
      <linearGradient id="platter" x1="0" y1="0" x2="1" y2="1">
        <stop offset="0" stop-color="#e9b35a"/>
        <stop offset="0.45" stop-color="#c77f2e"/>
        <stop offset="0.8" stop-color="#b06a22"/>
        <stop offset="1" stop-color="#ddd6c4"/>
      </linearGradient>
    </defs>
    <polygon points="0,545 1200,262 1200,1012 0,1268" fill="url(#platter)" role="img" aria-label="Photo: plate of cornmeal-fried catfish fillets with fries, hush puppies and tartar sauce"/>
    <polygon points="0,520 1200,238 1200,268 0,552" fill="var(--green)"/>
    <polygon points="0,1262 1200,1006 1200,1036 0,1294" fill="var(--green)"/>
  </svg>

  <div class="cut-line"></div>

  <header class="title-block">
    <h1 class="title">FRIED CATFISH</h1>
    <p class="tagline">ALWAYS FRESH!</p>
  </header>

  <section class="features">
    <div class="feature">
      <svg class="utensils" viewBox="0 0 290 90" aria-hidden="true">
        <g fill="var(--utensil)">
          <rect x="70" y="6" width="36" height="4"/><rect x="70" y="13" width="36" height="4"/><rect x="70" y="20" width="36" height="4"/><rect x="70" y="27" width="36" height="4"/>
          <path d="M104 6 h8 q6 0 8 8 v6 q-2 11 -8 11 h-8z"/>
          <rect x="118" y="15" width="160" height="8" rx="3"/>
          <ellipse cx="40" cy="66" rx="28" ry="16"/>
          <rect x="60" y="62" width="165" height="8" rx="3"/>
        </g>
      </svg>
      <p class="feature-text">MADE FROM SCRATCH</p>
    </div>
    <div class="feature">
      <svg class="utensils" viewBox="0 0 290 90" aria-hidden="true">
        <g fill="var(--utensil)">
          <rect x="70" y="6" width="36" height="4"/><rect x="70" y="13" width="36" height="4"/><rect x="70" y="20" width="36" height="4"/><rect x="70" y="27" width="36" height="4"/>
          <path d="M104 6 h8 q6 0 8 8 v6 q-2 11 -8 11 h-8z"/>
          <rect x="118" y="15" width="160" height="8" rx="3"/>
          <ellipse cx="40" cy="66" rx="28" ry="16"/>
          <rect x="60" y="62" width="165" height="8" rx="3"/>
        </g>
      </svg>
      <p class="feature-text">HAND-CUT FILLETS</p>
    </div>
    <div class="feature">
      <svg class="utensils" viewBox="0 0 290 90" aria-hidden="true">
        <g fill="var(--utensil)">
          <rect x="70" y="6" width="36" height="4"/><rect x="70" y="13" width="36" height="4"/><rect x="70" y="20" width="36" height="4"/><rect x="70" y="27" width="36" height="4"/>
          <path d="M104 6 h8 q6 0 8 8 v6 q-2 11 -8 11 h-8z"/>
          <rect x="118" y="15" width="160" height="8" rx="3"/>
          <ellipse cx="40" cy="66" rx="28" ry="16"/>
          <rect x="60" y="62" width="165" height="8" rx="3"/>
        </g>
      </svg>
      <p class="feature-text">THE BEST CATFISH IN TEXAS</p>
    </div>
    <div class="feature">
      <svg class="utensils" viewBox="0 0 290 90" aria-hidden="true">
        <g fill="var(--utensil)">
          <rect x="70" y="6" width="36" height="4"/><rect x="70" y="13" width="36" height="4"/><rect x="70" y="20" width="36" height="4"/><rect x="70" y="27" width="36" height="4"/>
          <path d="M104 6 h8 q6 0 8 8 v6 q-2 11 -8 11 h-8z"/>
          <rect x="118" y="15" width="160" height="8" rx="3"/>
          <ellipse cx="40" cy="66" rx="28" ry="16"/>
          <rect x="60" y="62" width="165" height="8" rx="3"/>
        </g>
      </svg>
      <p class="feature-text">SERVED WITH FRIES, HUSH PUPPIES<br>AND A 32OZ FOUNTAIN DRINK</p>
    </div>
  </section>

  <footer class="footer-band">ALSO AVAILABLE BY THE POUND!</footer>
</main>
</body>
</html>
```